International Psychology Practitioner, Educator and Researcher

I need a new website (or upgrade from existing square space. I provide innovative, client focused, services that are evidence based, specializing in crisis intervention, addiction and other mental health. I am also a researcher and university professor committed to excellence in education. I’m building on an existing practice (www.tidewillow.ca) and incorporating my personal/professional grade. I would like to see designs that use neutral colours and that incorporate crisp clear lines in a professional and inviting way. The final design should communicate professionalism and approachability. (New head shots and stills to follow)

Target Market(s)

Seeking therapy

Industry/Entity Type

Psychology

Coding

Coded - Design and coding required

Number of Pages Required

3 page

Font styles to use
Sans Serif

Requirements
Must have
• A friendly, warm, crisp feel - professional
Nice to have
• Each tones

```html
<!DOCTYPE html>
<html lang="en">
<head>
<meta charset="utf-8">
<title>Tidewillow.ca — Psychology &amp; Counselling</title>
<link href="https://fonts.googleapis.com/css2?family=Poppins:wght@300;400;500;600;700;800&family=Cormorant+Garamond:wght@500&display=swap" rel="stylesheet">
<style>
  :root{
    --ink:#2e2f2d;
    --muted:#5b5c58;
    --sand:#ebe4d8;
    --taupe:#9a8470;
    --deep:#55625d;
    --stone:#d9d2c6;
    --white:#fff;
    --black:#1d201f;
  }
  *{margin:0;padding:0;box-sizing:border-box}
  html,body{width:1200px;height:4068px;overflow:hidden;background:var(--white)}
  body{position:relative;font-family:"Poppins",sans-serif;color:var(--ink)}
  .abs{position:absolute}
  .shape{position:absolute;left:0;top:0}

  /* header */
  .logo{position:absolute;font-weight:500;color:var(--ink);letter-spacing:.5px}
  .logo-head{left:90px;top:28px;font-size:30px;border-bottom:2px solid var(--ink);padding-bottom:4px}
  .nav{position:absolute;left:470px;top:40px;display:flex;gap:28px;font-size:14px;font-weight:500;text-transform:uppercase}
  .btn{display:inline-flex;align-items:center;justify-content:center;gap:14px;font-weight:600;text-transform:uppercase;color:var(--white);letter-spacing:.3px}
  .btn-contact{position:absolute;left:968px;top:30px;width:142px;height:38px;background:var(--taupe);font-size:13px}

  /* hero */
  .hero-title{left:90px;top:300px;font-size:72px;line-height:70px;color:var(--ink)}
  .hero-title .light{font-weight:400}
  .hero-title b{font-weight:800}
  .hero-link{left:90px;top:578px;font-size:19px;font-weight:500;display:flex;gap:22px;align-items:center}
  .hero-link span{border-bottom:1.5px solid var(--ink);padding-bottom:2px}
  .hero-photo{left:627px;top:166px;width:573px;height:668px;background:linear-gradient(160deg,#dcd7cf 0%,#c4bdb2 45%,#8f8a84 75%,#4a4744 100%)}

  /* intro */
  .intro{left:0;top:960px;width:1200px;text-align:center}
  .intro h2{font-size:64px;line-height:64px;font-weight:600}
  .intro h2 .second{font-weight:500}
  .intro h2 em{font-style:normal;color:var(--taupe);font-weight:400}
  .intro p{margin-top:18px;font-size:23px;line-height:34px;font-weight:400}

  /* services */
  .services-title{left:0;top:1394px;width:1200px;text-align:center;color:var(--white);font-size:64px;font-weight:400}
  .services-title b{font-weight:800}
  .card{position:absolute;top:1495px;width:330px;height:384px;background:var(--white);padding:44px 36px 0;box-shadow:0 10px 30px rgba(0,0,0,.07)}
  .card-icon{width:84px;height:84px;border-radius:10px;background:linear-gradient(135deg,#efe9df,#cdbfae)}
  .card h3{margin-top:20px;font-size:23px;line-height:27px;font-weight:700}
  .card p{margin-top:12px;font-size:14.5px;line-height:26px;color:var(--muted)}
  .card .arrow{margin-top:10px}
  .btn-book{position:absolute;left:491px;top:1930px;width:218px;height:44px;background:var(--taupe);font-size:14px}

  /* dream big */
  .dream{left:0;top:2140px;width:1200px;text-align:center}
  .dream h2{font-size:92px;font-weight:700;line-height:110px}
  .dream h2 em{font-style:normal;color:var(--taupe)}
  .dream p{font-size:23px;line-height:32px}
  .quote{left:587px;top:2410px;font-size:34px;line-height:48px;font-weight:400}
  .quote-by{left:587px;top:2568px;font-size:18px}

  /* video */
  .video{left:88px;top:2727px;width:1022px;height:473px;background:var(--black)}
  .play{left:567px;top:2828px;width:66px;height:66px;background:var(--deep)}
  .video-rule{position:absolute;left:322px;width:553px;height:4px;background:var(--taupe)}
  .video-brand{left:0;top:2938px;width:1200px;text-align:center;font-family:"Cormorant Garamond",serif;color:var(--white);font-size:54px;letter-spacing:4px}
  .video-sub{left:0;top:3046px;width:1200px;text-align:center;font-family:"Cormorant Garamond",serif;color:var(--white);font-size:30px;letter-spacing:12px;line-height:34px}

  /* cta */
  .cta{left:0;top:3310px;width:1200px;height:364px;background:var(--taupe);text-align:center;color:var(--white)}
  .cta h2{margin-top:94px;font-size:66px;font-weight:700;line-height:80px}
  .cta p{font-size:23px;margin-top:2px}
  .btn-schedule{margin-top:14px;width:276px;height:44px;background:var(--deep);font-size:14px}

  /* footer */
  .logo-foot{left:90px;top:3796px;font-size:36px;border-bottom:2px solid var(--ink);padding-bottom:6px}
  .foot-col{position:absolute;top:3796px;font-size:14.5px;line-height:22px}
  .foot-col h4{font-size:23px;font-weight:600;line-height:34px;margin-bottom:2px}
  .foot-col .gap{height:10px}
  .foot-col a{color:var(--deep);text-decoration:underline}
  .map{left:430px;top:3860px;width:210px;height:120px;background:radial-gradient(ellipse at center,#eeebe6 0%,rgba(255,255,255,0) 70%)}
  .foot-rule{left:88px;top:4019px;width:1022px;height:1px;background:#ccc}
  .copyright{left:88px;top:4033px;font-size:13px}
  .social{position:absolute;top:4035px;width:16px;height:16px;border:2px solid var(--ink);border-radius:3px}
  .to-top{left:1140px;top:4000px;width:32px;height:32px;border-radius:50%;background:var(--taupe)}
</style>
</head>
<body>

<svg class="shape" width="1200" height="840" viewBox="0 0 1200 840" aria-hidden="true">
  <path d="M790 0 H1200 V166 H1000 C880 166 860 150 800 150 C760 150 790 80 790 0 Z" fill="var(--sand)"/>
  <path d="M0 410 C200 400 400 300 627 240 V560 C560 600 530 680 530 787 H0 Z" fill="var(--sand)"/>
  <path d="M573 636 V880 H819" stroke="var(--taupe)" stroke-width="2" fill="none"/>
</svg>

<header>
  <div class="logo logo-head">Tidewillow.ca</div>
  <nav class="nav"><span>Home</span><span>About us</span><span>Our services</span><span>Corporate clients</span></nav>
  <span class="btn btn-contact">Contact us</span>
</header>

<section class="hero">
  <div class="abs hero-photo" role="img" aria-label="Photo of a distressed woman sitting on a sofa holding her head"></div>
  <h1 class="abs hero-title"><span class="light">Get ready</span><br><b>to take control of<br>your life.</b></h1>
  <div class="abs hero-link"><span>Schedule a Consultation Today</span>
    <svg width="20" height="12" viewBox="0 0 20 12"><path d="M0 6H18M13 1l5 5-5 5" stroke="#2e2f2d" stroke-width="1.5" fill="none"/></svg></div>
</section>

<section class="abs intro">
  <h2>After just<br><span class="second"><em>one</em> session,</span></h2>
  <p>you’ll feel more in control of your life, relationships,<br>career and future goals.</p>
</section>

<svg class="shape" width="1200" height="4068" viewBox="0 0 1200 4068" aria-hidden="true" style="pointer-events:none">
  <path d="M0 1284 H1200 V1500 C1150 1482 1110 1492 1100 1505 V1880 H470 C440 1900 428 1960 430 2050 H0 Z" fill="var(--deep)"/>
</svg>

<h2 class="abs services-title"><b>Our</b> Services</h2>

<article class="card" style="left:88px">
  <div class="card-icon" role="img" aria-label="Icon of a person with a heart"></div>
  <h3>Individual Therapy<br>for Life</h3>
  <p>Evidence based therapy with a psych-ologist who helps you understand your needs and build a plan to move forward.</p>
  <svg class="arrow" width="20" height="12" viewBox="0 0 20 12"><path d="M0 6H18M13 1l5 5-5 5" stroke="#2e2f2d" stroke-width="1.5" fill="none"/></svg>
</article>
<article class="card" style="left:436px">
  <div class="card-icon" role="img" aria-label="Icon of a handshake inside a heart"></div>
  <h3>Crisis Intervention<br>&amp; Support</h3>
  <p>Calm, client focused support in diff-icult moments, helping you regain stability and find a safe next step.</p>
  <svg class="arrow" width="20" height="12" viewBox="0 0 20 12"><path d="M0 6H18M13 1l5 5-5 5" stroke="#2e2f2d" stroke-width="1.5" fill="none"/></svg>
</article>
<article class="card" style="left:785px">
  <div class="card-icon" role="img" aria-label="Icon of two people talking"></div>
  <h3>Addiction &amp;<br>Mental Health</h3>
  <p>Have you ever wondered - what next - when it comes to recovery? &nbsp;Well you are not alone! We provide solution-focused...</p>
  <svg class="arrow" width="20" height="12" viewBox="0 0 20 12"><path d="M0 6H18M13 1l5 5-5 5" stroke="#2e2f2d" stroke-width="1.5" fill="none"/></svg>
</article>

<span class="btn btn-book">Book a consult
  <svg width="18" height="12" viewBox="0 0 20 12"><path d="M0 6H18M13 1l5 5-5 5" stroke="#fff" stroke-width="1.5" fill="none"/></svg></span>

<section class="abs dream">
  <h2><em>Dream</em> Big.</h2>
  <p>Do What’s Right Not What’s Easy.<br>Finish What you Start.</p>
</section>

<svg class="abs" style="left:150px;top:2334px" width="394" height="334" viewBox="0 0 394 334" role="img" aria-label="Portrait photo of a smiling client against a warm neutral background">
  <defs><linearGradient id="portrait" x1="0" y1="0" x2="1" y2="1"><stop offset="0" stop-color="#d9cbb8"/><stop offset="1" stop-color="#b39c84"/></linearGradient></defs>
  <path d="M140 0 C250 0 360 80 390 190 C410 280 320 334 230 334 C120 334 0 290 0 170 C0 70 50 0 140 0 Z" fill="url(#portrait)"/>
</svg>

<p class="abs quote">“I dreamed big!<br>I’m now in my dream career<br>living my best life”</p>
<p class="abs quote-by">– Maya R.</p>

<section>
  <div class="abs video"></div>
  <svg class="abs play" viewBox="0 0 66 66"><path d="M25 21 L46 33 L25 45 Z" fill="#fff"/></svg>
  <div class="video-rule" style="top:2916px"></div>
  <div class="abs video-brand">TIDEWILLOW.CA</div>
  <div class="video-rule" style="top:3018px"></div>
  <div class="abs video-sub">LIFE &amp; CAREER<br>COACHING</div>
</section>

<section class="abs cta">
  <h2>Let’s Talk!</h2>
  <p>Your first discovery consultation is free.</p>
  <span class="btn btn-schedule">Schedule a consultation</span>
</section>

<footer>
  <div class="logo logo-foot">Tidewillow.ca</div>
  <div class="abs map" role="img" aria-label="Faint world map"></div>
  <div class="foot-col" style="left:423px">
    <h4>Location</h4>
    <p>1-118 Harbour Lane<br>Duncan, BC, Canada</p>
  </div>
  <div class="foot-col" style="left:676px">
    <h4>Hours</h4>
    <p>Monday — Friday<br>9am — 5pm</p>
    <div class="gap"></div>
    <p>Saturday<br>9am — 1pm</p>
  </div>
  <div class="foot-col" style="left:892px">
    <h4>Contact</h4>
    <p>hello@tidewillow.ca</p>
    <div class="gap" style="height:4px"></div>
    <p>(250) 555-0148</p>
    <div class="gap"></div>
    <p><a>Schedule an Appointment</a></p>
  </div>
  <div class="abs foot-rule"></div>
  <p class="abs copyright">©Copyright 2021 | All Rights Reserved</p>
  <span class="social" style="left:1067px"></span>
  <span class="social" style="left:1094px"></span>
  <svg class="abs to-top" viewBox="0 0 32 32"><path d="M11 18l5-5 5 5" stroke="#fff" stroke-width="2" fill="none"/></svg>
</footer>

</body>
</html>
```